Flyer for a marketing

We are a holistic mental health facility in need of a flyer to help promote our services and encourage more people to seek care. See the attachment to tell you more. We prefer warm green colors or rich blue. Thank you.

```html
<!DOCTYPE html>
<html lang="en">
<head>
<meta charset="utf-8">
<title>Clearwater Mind Health and Wellness – Flyer</title>
<link rel="stylesheet" href="https://fonts.googleapis.com/css2?family=Bebas+Neue&family=Poppins:wght@400;500;600;700&display=swap">
<style>
:root{
  --blue:#0b78ad;
  --blue-dark:#0a6a99;
  --green:#2f7139;
  --green-dark:#2c5a3b;
  --white:#ffffff;
  --ink:#1f2a2e;
  --page:#e4e4e4;
  --photo-a:#d9c4b4;
  --photo-b:#8fa4a8;
}
*{margin:0;padding:0;box-sizing:border-box}
html,body{width:1200px;height:2400px;overflow:hidden}
body{background:var(--page);font-family:"Poppins",sans-serif;color:var(--ink);position:relative}
.flyer{position:absolute;left:0;top:424px;width:1200px;height:1553px;background:var(--white);overflow:hidden}
.abs{position:absolute}

.hero-backdrop{left:578px;top:0;width:622px;height:694px;background:var(--green);border-bottom-left-radius:70px}
.hero-photo{left:613px;top:93px;width:523px;height:549px;border-radius:46px;background:linear-gradient(160deg,#eef0ee 0%,var(--photo-a) 45%,var(--photo-b) 100%)}

.brand{left:64px;top:92px;display:flex;align-items:center;gap:26px}
.brand-dot{width:96px;height:96px;border-radius:50%;background:var(--green)}
.brand-name{font-family:"Poppins",sans-serif;font-weight:600;font-size:34px;line-height:1.08;color:var(--green)}

.headline-band{left:0;top:286px;width:613px;height:373px;background:var(--blue);border-bottom-right-radius:30px}
.headline-top{left:63px;top:305px;font-family:"Poppins",sans-serif;font-weight:600;font-size:76px;line-height:1;color:var(--white);letter-spacing:1px}
.headline-main{left:63px;top:385px;font-family:"Bebas Neue",sans-serif;font-size:118px;line-height:1;color:var(--white);letter-spacing:-1px}
.headline-dash{left:63px;top:504px;width:28px;height:5px;background:var(--white)}
.headline-sub{left:63px;top:528px;width:520px;font-size:25px;line-height:30px;color:var(--white)}

.why-title{left:70px;top:700px;font-size:30px;font-weight:700;color:var(--green);letter-spacing:.3px}
.why-title span{color:var(--blue)}

.reason{left:64px;width:470px;height:100px}
.reason-pill{position:absolute;left:60px;top:20px;width:390px;height:74px;border-radius:0 30px 30px 0;display:flex;align-items:center;padding-left:68px;padding-right:14px;font-size:17px;line-height:20px;color:var(--white);box-shadow:4px 6px 8px rgba(0,0,0,.18)}
.reason-icon{position:absolute;left:0;top:0;width:100px;height:100px;border-radius:50%;background:var(--white);border:5px solid var(--blue);box-shadow:0 4px 8px rgba(0,0,0,.2);display:flex;align-items:center;justify-content:center}
.reason.is-blue .reason-pill{background:var(--blue)}
.reason.is-green .reason-pill{background:var(--green-dark)}
.reason.is-green .reason-icon{border-color:var(--green-dark)}
.reason-icon svg{width:50px;height:50px}

.accepting{left:592px;top:735px;font-size:25.5px;line-height:33px;font-weight:700;color:var(--green);letter-spacing:.2px}
.accepting span{color:var(--blue)}
.accepting-copy{left:595px;top:818px;width:200px;font-size:22.5px;line-height:28.5px;color:var(--ink)}
.clinic-photo{left:815px;top:809px;width:320px;height:183px;border:3px solid var(--blue);border-radius:20px;background:linear-gradient(135deg,#f1f4f6 0%,#c9d6e2 50%,#6f9cc4 100%)}

.services{left:592px;top:1034px;width:543px;height:292px;border-radius:28px;background:var(--green)}
.services-tab{position:absolute;left:161px;top:0;width:233px;height:40px;background:var(--white);border-radius:0 0 20px 20px;display:flex;align-items:center;justify-content:center;font-size:20px;font-weight:600;letter-spacing:3px;color:var(--blue)}
.service{position:absolute;width:180px;margin-left:-90px;text-align:center;color:var(--white);font-size:13.5px;line-height:16px}
.service-icon{width:52px;height:52px;margin:0 auto 8px;border-radius:50%;background:var(--white);border:3px solid #cfe0e8;display:flex;align-items:center;justify-content:center}
.service-icon svg{width:28px;height:28px}
.services-rule{position:absolute;width:0;border-left:1.5px dashed rgba(255,255,255,.6)}

.footer-title{left:63px;top:1377px;width:1072px;display:flex;align-items:center;gap:14px;font-size:24.5px;font-weight:700;color:var(--blue);white-space:nowrap}
.footer-title::after{content:"";flex:1;height:1.5px;background:var(--blue)}
.contact{top:1430px;font-size:21.5px;line-height:28px;color:var(--ink)}
.contact-row{display:flex;align-items:center;gap:12px}
.contact svg{width:18px;height:18px;flex:none}
.contact-divider{top:1432px;width:0;height:56px;border-left:1.5px dashed #9aa4a8}
</style>
</head>
<body>
<main class="flyer">
  <div class="abs hero-backdrop"></div>
  <div class="abs hero-photo" role="img" aria-label="Photo of a smiling family: a father carrying his young daughter on his shoulders beside the mother"></div>

  <div class="abs brand">
    <div class="brand-dot"></div>
    <div class="brand-name">Clearwater<br>Mind<br>Health and<br>Wellness</div>
  </div>

  <div class="abs headline-band"></div>
  <h1 class="abs headline-top">THE CARE</h1>
  <div class="abs headline-main">YOU DESERVE</div>
  <div class="abs headline-dash"></div>
  <p class="abs headline-sub">Clearwater Mind Health &amp; Wellness, where deserving patients meet compassionate providers</p>

  <h2 class="abs why-title">WHY <span>CHOOSE US?</span></h2>

  <div class="abs reason is-blue" style="top:761px">
    <div class="reason-pill">We are an integrative holistic<br>psychiatric center.</div>
    <div class="reason-icon"><svg viewBox="0 0 50 50" fill="none" stroke="#0b78ad" stroke-width="2.5" stroke-linecap="round" stroke-linejoin="round"><path d="M25 10c4 4 5 9 0 15-5-6-4-11 0-15z"/><path d="M17 16c5 1 8 5 8 9-5 0-9-3-8-9zM33 16c-5 1-8 5-8 9 5 0 9-3 8-9z"/><path d="M8 22v12l8 8M42 22v12l-8 8"/></svg></div>
  </div>
  <div class="abs reason is-green" style="top:872px">
    <div class="reason-pill">Our mission is to provide<br>compassionate quality care.</div>
    <div class="reason-icon"><svg viewBox="0 0 50 50" fill="none" stroke="#0b78ad" stroke-width="2.5" stroke-linecap="round" stroke-linejoin="round"><circle cx="27" cy="17" r="8"/><path d="M23 17l3 3 5-6"/><path d="M8 36l8-6h10l8 4 8-6M8 42h24l10-8"/></svg></div>
  </div>
  <div class="abs reason is-blue" style="top:989px">
    <div class="reason-pill">We provide psychiatric services<br>including medication<br>management &amp; psychotherapy.</div>
    <div class="reason-icon"><svg viewBox="0 0 50 50" fill="none" stroke="#1f2a2e" stroke-width="2.5" stroke-linecap="round" stroke-linejoin="round"><circle cx="34" cy="10" r="4"/><path d="M34 16v14l-4 12M34 30l4 12M28 22l6-4 6 6"/><circle cx="16" cy="36" r="7"/><circle cx="14" cy="16" r="3"/><path d="M14 20v10h8"/></svg></div>
  </div>
  <div class="abs reason is-green" style="top:1105px">
    <div class="reason-pill">We listen, care, and empower<br>you to live better.</div>
    <div class="reason-icon"><svg viewBox="0 0 50 50" fill="none" stroke="#0b78ad" stroke-width="2.5" stroke-linecap="round" stroke-linejoin="round"><path d="M25 40S10 30 10 21a7 7 0 0 1 15-3 7 7 0 0 1 15 3c0 9-15 19-15 19z"/><path d="M19 25l4 4 8-8"/><path d="M36 6v8M32 10h8"/></svg></div>
  </div>
  <div class="abs reason is-blue" style="top:1226px">
    <div class="reason-pill">We accept major insurances.</div>
    <div class="reason-icon"><svg viewBox="0 0 50 50" fill="none" stroke="#2c5a3b" stroke-width="2.5" stroke-linecap="round" stroke-linejoin="round"><path d="M25 6l11 4v9c0 7-5 12-11 14-6-2-11-7-11-14v-9z"/><path d="M20 19l4 4 7-7"/><path d="M6 30v8l8 6M44 30v8l-8 6"/></svg></div>
  </div>

  <h2 class="abs accepting">WE ARE ACCEPTING NEW PATIENTS,<br><span>NO WAITING LIST</span></h2>
  <p class="abs accepting-copy">Your mental health matters, so make it a priority and call us today for an appointment.</p>
  <div class="abs clinic-photo" role="img" aria-label="Photo of a doctor in a white coat consulting with a colleague at a computer in a clinic office"></div>

  <section class="abs services">
    <div class="services-tab">OUR SERVICES</div>
    <div class="services-rule" style="left:188px;top:52px;height:90px"></div>
    <div class="services-rule" style="left:381px;top:52px;height:90px"></div>
    <div class="services-rule" style="left:276px;top:172px;height:92px"></div>

    <div class="service" style="left:97px;top:54px">
      <div class="service-icon"><svg viewBox="0 0 28 28" fill="none" stroke="#0b78ad" stroke-width="2" stroke-linecap="round"><circle cx="14" cy="14" r="9"/><path d="M14 9v5l4 3"/></svg></div>
      Comprehensive<br>Psychiatric Evaluation
    </div>
    <div class="service" style="left:278px;top:54px">
      <div class="service-icon"><svg viewBox="0 0 28 28" fill="none" stroke="#0b78ad" stroke-width="2" stroke-linecap="round"><circle cx="14" cy="14" r="4"/><path d="M14 4v4M14 20v4M4 14h4M20 14h4M7 7l3 3M18 18l3 3M21 7l-3 3M10 18l-3 3"/></svg></div>
      Integrative<br>Psychotherapy session
    </div>
    <div class="service" style="left:459px;top:54px">
      <div class="service-icon"><svg viewBox="0 0 28 28" fill="none" stroke="#0b78ad" stroke-width="2" stroke-linecap="round"><path d="M14 4v20M9 9c3-2 7-2 10 0M10 14c3 2 5 2 8 0M10 19c3-2 5-2 8 0"/></svg></div>
      Medication<br>management
    </div>
    <div class="service" style="left:161px;top:171px">
      <div class="service-icon"><svg viewBox="0 0 28 28" fill="none" stroke="#0b78ad" stroke-width="2" stroke-linecap="round"><circle cx="17" cy="6" r="2.5"/><path d="M17 10v8l-2 6M17 18l2 6"/><circle cx="9" cy="19" r="4"/></svg></div>
      Ketamine<br>Assisted Psychotherapy
    </div>
    <div class="service" style="left:389px;top:171px">
      <div class="service-icon"><svg viewBox="0 0 28 28" fill="none" stroke="#0b78ad" stroke-width="2" stroke-linecap="round" stroke-linejoin="round"><path d="M14 4l8 3v6c0 5-4 9-8 10-4-1-8-5-8-10V7z"/><circle cx="14" cy="13" r="3"/></svg></div>
      Medication management<br>with psychotherapy
    </div>
  </section>

  <h3 class="abs footer-title">CLEARWATER MIND HEALTH AND WELLNESS, APNC</h3>

  <div class="abs contact" style="left:63px">
    <div class="contact-row" style="align-items:flex-start">
      <svg viewBox="0 0 18 18" style="margin-top:5px"><path d="M9 1a6 6 0 0 0-6 6c0 4.5 6 10 6 10s6-5.5 6-10a6 6 0 0 0-6-6z" fill="#2f7139"/><circle cx="9" cy="7" r="2.2" fill="#fff"/></svg>
      <span>4815 Maple Grove Road,<br>Suite 120 Fairview, CA 90000</span>
    </div>
  </div>
  <div class="abs contact-divider" style="left:429px"></div>
  <div class="abs contact" style="left:463px">
    <div class="contact-row">
      <svg viewBox="0 0 18 18"><circle cx="9" cy="9" r="9" fill="#2f7139"/><path d="M6 4.5l2 2.2-1 1.2c.7 1.4 1.7 2.4 3 3l1.2-1 2.2 2-1 1.6c-3.8-.4-6.6-3.2-7-7z" fill="#fff"/></svg>
      <span>(555) 214-7730</span>
    </div>
    <div class="contact-row">
      <svg viewBox="0 0 18 18"><circle cx="9" cy="9" r="9" fill="#2f7139"/><rect x="5" y="7" width="8" height="5" rx="1" fill="#fff"/><rect x="6.5" y="4.5" width="5" height="3" fill="#fff"/></svg>
      <span>(555) 309-4418</span>
    </div>
  </div>
  <div class="abs contact-divider" style="left:697px"></div>
  <div class="abs contact" style="left:732px">
    <div class="contact-row">
      <svg viewBox="0 0 18 18"><circle cx="9" cy="9" r="9" fill="#2f7139"/><rect x="4.5" y="5.5" width="9" height="7" rx="1" fill="#fff"/><path d="M4.5 6l4.5 3.5L13.5 6" stroke="#2f7139" stroke-width="1.2" fill="none"/></svg>
      <span>info@clearwatermindhealth.com</span>
    </div>
    <div class="contact-row">
      <svg viewBox="0 0 18 18"><circle cx="9" cy="9" r="9" fill="#2f7139"/><circle cx="9" cy="9" r="5" fill="none" stroke="#fff" stroke-width="1.3"/><path d="M4 9h10M9 4c-2 3-2 7 0 10M9 4c2 3 2 7 0 10" stroke="#fff" stroke-width="1.1" fill="none"/></svg>
      <span>www.clearwatermindhealth.com</span>
    </div>
  </div>
</main>
</body>
</html>
```